Aviation: Overcast Study Guide Book Cover

We need a book cover (front and back) designed for an Instrument Flight Rules (IFR) study guide used by helicopter and airplane pilots to obtain an instrument rating for a helicopter or airplane. Below is the title and subtitles.

TITLE: OVERCAST STUDY GUIDE
SUBTITLE 1: Checkride Preparation for Airplane and Helicopter Pilots
SUBTITLE 2: Prepare for your Instrument Rating with Confidence

We have also upload recommended text to be included on the back cover. In addition, we included images of similar book covers that we like and ones that we do not like. Below are links to two others books by the author.

https://www.bookvarro.example/Rotorcraft-Exam-Handbook-oral-review/dp/507214638K
https://www.bookvarro.example/Manual-Floatwing-Handling-Lionel-Quarrick/dp/5093742816

Flight students

Aviation

• helicopter and airplane

```html
<!DOCTYPE html>
<html lang="en">
<head>
<meta charset="utf-8">
<title>Overcast Study Guide – Cover Spread</title>
<link href="https://fonts.googleapis.com/css2?family=Cinzel:wght@500;600&family=Marcellus&family=Crimson+Text:wght@400;600;700&display=swap" rel="stylesheet">
<style>
  :root{
    --bg:#4f4f4f;
    --paper:#ffffff;
    --red:#e81e25;
    --ink:#1d1d1d;
    --text:#222222;
    --photo-slot:#a4acb4;
    --sky-a:#3e5066;
    --sky-b:#8b97a6;
    --cloud:#dfe3e8;
  }
  *{margin:0;padding:0;box-sizing:border-box}
  html,body{width:1200px;height:1188px;overflow:hidden;background:var(--bg)}
  .spread{position:absolute;left:95px;top:240px;width:1009px;height:698px;background:var(--paper);color:var(--text);font-family:"Crimson Text",serif}
  .band-top{position:absolute;left:0;top:0;width:100%;height:27px;background:var(--red)}
  .band-bottom{position:absolute;left:0;bottom:0;width:100%;height:11px;background:var(--red)}

  /* back cover */
  .back-title{position:absolute;left:20px;width:452px;top:52px;text-align:center;font-family:"Marcellus",serif;font-size:31px;color:var(--ink);letter-spacing:-.3px}
  .back-tagline{position:absolute;left:20px;width:452px;top:97px;text-align:center;font-size:13px}
  .back-copy{position:absolute;left:59px;width:374px;top:125px;font-size:9.8px;line-height:12.4px;text-align:justify}
  .back-copy p{margin-bottom:12px}
  .back-copy p.tight{margin-bottom:0}
  .topics{position:absolute;left:58px;top:270px;width:375px;height:72px;border:1px solid var(--red);border-radius:7px;overflow:hidden;display:grid;grid-template-columns:130px 122px 1fr;grid-template-rows:repeat(3,1fr)}
  .topics li{list-style:none;font-size:9.6px;font-weight:600;display:flex;align-items:center;padding-left:8px;border-right:1px solid var(--red);border-bottom:1px solid var(--red)}
  .topics li:nth-child(3n){border-right:none}
  .topics li:nth-child(n+7){border-bottom:none}
  .topics li::before{content:"•";margin-right:4px}
  .back-author{position:absolute;left:20px;width:452px;top:355px;text-align:center;font-family:"Cinzel",serif;font-weight:500;font-size:24px;color:var(--ink)}
  .author-photo{position:absolute;left:50px;top:403px;width:124px;height:183px;background:var(--photo-slot)}
  .author-bio{position:absolute;left:189px;width:244px;top:400px;font-size:9.6px;line-height:12.4px;text-align:justify}

  /* spine */
  .spine-text{position:absolute;left:502px;transform:translate(-50%,-50%) rotate(-90deg);white-space:nowrap;color:var(--ink)}
  .spine-author{top:120px;font-family:"Cinzel",serif;font-size:8.5px;letter-spacing:1.6px}
  .spine-subtitle{top:348px;font-size:9.4px}
  .spine-title{top:572px;font-family:"Cinzel",serif;font-size:9.5px;letter-spacing:2.4px}

  /* front cover */
  .front-title{position:absolute;left:517px;width:492px;top:58px;text-align:center;color:var(--ink)}
  .front-title .main{display:block;font-family:"Cinzel",serif;font-weight:600;font-size:76px;line-height:100px;letter-spacing:-1px}
  .front-title .sub{display:block;font-family:"Marcellus",serif;font-size:48px;line-height:48px;margin-top:-2px}
  .front-subtitle{position:absolute;left:517px;width:492px;top:268px;text-align:center;font-weight:700;font-size:16px}
  .front-tagline{position:absolute;left:517px;width:492px;top:295px;text-align:center;font-size:14px}
  .front-photo{position:absolute;left:517px;top:333px;width:492px;height:259px;border-top:3px solid var(--red);border-bottom:3px solid var(--red);background:linear-gradient(180deg,var(--sky-a) 0%,var(--sky-b) 30%,var(--cloud) 60%,#5a5e66 100%)}
  .front-author{position:absolute;left:517px;width:492px;top:625px;text-align:center;font-family:"Cinzel",serif;font-weight:500;font-size:26px;color:var(--ink)}
</style>
</head>
<body>
<main class="spread">
  <div class="band-top"></div>

  <section class="back-cover">
    <h2 class="back-title">OVERCAST STUDY GUIDE</h2>
    <p class="back-tagline">Prepare for your IFR check ride with confidence</p>
    <div class="back-copy">
      <p>Becoming an instrument rated pilot is one of the most challenging ratings to obtain. This guide helps prepare you to pass your IFR check ride with confidence. The question-and-answer format is easy to follow and provides detailed explanations for expanded knowledge.</p>
      <p class="tight">Includes Helicopter and Airplane Specific Content</p>
      <p>This guide is designed to prepare an airplane or helicopter pilot the oral portion of the IFR checkride. Unlike other resources, this guide specifically addresses the differences with IFR flight in helicopters. As a dual rated pilot, the author ensures to identify areas of differences between the two categories of IFR flight. The following concepts are addressed within the guide.</p>
    </div>
    <ul class="topics">
      <li>Preflight Actions</li><li>Enroute Procedures</li><li>Aeromedical Factors</li>
      <li>General IFR Concepts</li><li>Approach Procedures</li><li>Weather Fundamentals</li>
      <li>Departure Procedures</li><li>IFR Emergences</li><li>Risk Management</li>
    </ul>
    <p class="back-author">Harlan T. Weskett</p>
    <div class="author-photo" role="img" aria-label="Author portrait"></div>
    <p class="author-bio">About the Author: Harlan Weskett is ATP rated pilot and helicopter and fixed-wing instructor. Harlan is the owner and operator Northvale Crest, LLC which does business as Loftline Aviation and Pike Aviation. Loftline Aviation provides primary helicopter flight instruction while Pike Aviation provides seaplane flight instruction and tours. In addition to instructing, Harlan has authored other books to include. The Rotorcraft Exam Handbook, and Manual of Floatwing Handling. Harlan lives in Kentucky with his beautiful wife Marisa. They have a daughter, Clara, that is dual rated and employed as a captain for a charter company. Prior to learning to fly, Harlan spent several years in the military as a Special Warfare Combat Craft Crewman in the U.S. Navy and Ranger-qualified infantry officer in the U.S. Army.</p>
  </section>

  <section class="spine">
    <span class="spine-text spine-author">HARLAN T. WESKETT</span>
    <span class="spine-text spine-subtitle">Checkride Preparation for Airplane and Helicopter Pilots</span>
    <span class="spine-text spine-title">OVERCAST STUDY GUIDE</span>
  </section>

  <section class="front-cover">
    <h1 class="front-title"><span class="main">OVERCAST</span><span class="sub">STUDY GUIDE</span></h1>
    <p class="front-subtitle">Checkride Preparation for Airplane and Helicopter Pilots</p>
    <p class="front-tagline">Prepare for your Instrument Rating with Confidence</p>
    <div class="front-photo" role="img" aria-label="Helicopter cockpit view with pilot and glass instrument panel flying above a sea of clouds and mountains"></div>
    <p class="front-author">Harlan T. Weskett</p>
  </section>

  <div class="band-bottom"></div>
</main>
</body>
</html>
```